One of a kind service business!

We are the only ocean freight auditing company in the entire world that does what we do. We provide a innovative service in auditing our clients invoices for billing errors as it relates to the import and export of their products anywhere in the world. We'd like to retain the current logo - but we are open to any interesting concepts that can complete the card.

Target Market(s)

C-Level and Senior Financial executives

Industry/Entity Type

Auditing

Requirements
Must have

• ONE SIDED ONLY
Should not have
• no cartoonish images

```html
<!DOCTYPE html>
<html lang="en">
<head>
<meta charset="utf-8">
<title>Tidewater Review – Business Card</title>
<link rel="stylesheet" href="https://fonts.googleapis.com/css2?family=Open+Sans:wght@400;600&display=swap">
<style>
  :root {
    --backdrop: #d6d6d6;
    --card-white: #ffffff;
    --wave-blue: #2b80bf;
    --deep-navy: #152f5f;
    --ink: #222222;
    --icon-blue: #2a6fae;
    --brand-blue: #1d5e9c;
  }
  * { margin: 0; padding: 0; box-sizing: border-box; }
  html, body {
    width: 1200px; height: 944px; overflow: hidden;
    background: var(--backdrop);
    font-family: "Open Sans", Arial, sans-serif;
  }
  .canvas { position: relative; width: 1200px; height: 944px; }
  .business-card {
    position: absolute; left: 100px; top: 186px;
    width: 1000px; height: 572px;
    background: var(--card-white);
    border-radius: 29px;
    overflow: hidden;
    box-shadow: 0 10px 30px rgba(0,0,0,0.25);
  }
  .wave-bands { position: absolute; inset: 0; width: 100%; height: 100%; }
  .wave-light { fill: var(--wave-blue); }
  .wave-dark { fill: var(--deep-navy); }
  .brand-name {
    position: absolute; left: 48px; top: 86px;
    font-size: 56px; font-weight: 600; line-height: 1;
    color: var(--brand-blue); letter-spacing: 0.5px;
  }
  .contact-block {
    position: absolute; left: 72px;
    color: var(--ink); font-size: 27px; line-height: 34px;
  }
  .address-block { top: 210px; }
  .lines-block { top: 325px; }
  .contact-row { display: flex; align-items: center; height: 34px; }
  .contact-row .icon { width: 22px; height: 22px; margin-right: 18px; flex: none; fill: var(--icon-blue); }
  .contact-row.indent { padding-left: 40px; }
  .person {
    position: absolute; left: 801px; transform: translateX(-50%);
    text-align: center; color: #fff; white-space: nowrap;
  }
  .person-name { top: 452px; font-size: 38px; line-height: 46px; }
  .person-title { top: 502px; font-size: 26px; line-height: 30px; }
</style>
</head>
<body>
<div class="canvas">
  <div class="business-card">
    <svg class="wave-bands" viewBox="0 0 418 239" preserveAspectRatio="none" aria-hidden="true">
      <path class="wave-light" d="M255,0 C285,40 252,92 232,140 C216,180 208,215 205,239 L418,239 L418,0 Z"/>
      <path class="wave-dark" d="M300,0 C330,50 292,92 272,140 C257,180 250,215 245,239 L418,239 L418,0 Z"/>
    </svg>

    <div class="brand-name">Tidewater Review</div>

    <div class="contact-block address-block">
      <div class="contact-row">
        <svg class="icon" viewBox="0 0 20 20"><path d="M10 2 L19 10 H16 V18 H12 V13 H8 V18 H4 V10 H1 Z"/></svg>
        Harbor Business Park
      </div>
      <div class="contact-row indent">Lindenova 28, Prague</div>
      <div class="contact-row indent">Czech Republic 11000</div>
    </div>

    <div class="contact-block lines-block">
      <div class="contact-row">
        <svg class="icon" viewBox="0 0 20 20"><path d="M6 2 C4 3 3 6 4 9 C6 14 10 17 14 18 C16 18 17 17 18 15 L15 12 L13 14 C10 13 8 10 7 8 L9 6 Z"/></svg>
        +420 555 010 314
      </div>
      <div class="contact-row">
        <svg class="icon" viewBox="0 0 20 20"><path d="M6 1 H14 A1.5 1.5 0 0 1 15.5 2.5 V17.5 A1.5 1.5 0 0 1 14 19 H6 A1.5 1.5 0 0 1 4.5 17.5 V2.5 A1.5 1.5 0 0 1 6 1 Z M6.5 3.5 V14 H13.5 V3.5 Z"/></svg>
        +420 555 020 786
      </div>
      <div class="contact-row">
        <svg class="icon" viewBox="0 0 20 20"><path d="M6 2 C4 3 3 6 4 9 C6 14 10 17 14 18 C16 18 17 17 18 15 L15 12 L13 14 C10 13 8 10 7 8 L9 6 Z"/></svg>
        +1 555 014 2298 - USA
      </div>
      <div class="contact-row">
        <svg class="icon" viewBox="0 0 20 20"><path d="M5 2 H13 V7 H5 Z M2 8 H18 V16 H2 Z M5 13 H15 V18 H5 Z"/></svg>
        +420 555 030 900
      </div>
      <div class="contact-row">
        <svg class="icon" viewBox="0 0 20 20"><circle cx="10" cy="10" r="8.5"/></svg>
        www.tidewaterreview.net
      </div>
      <div class="contact-row">
        <svg class="icon" viewBox="0 0 20 20"><path d="M2 5 H18 V16 H2 Z M3 6 L10 11 L17 6" stroke="#fff" stroke-width="1.2"/></svg>
        daniel@tidewaterreview.net
      </div>
    </div>

    <div class="person person-name">Daniel Marsh</div>
    <div class="person person-title">CEO</div>
  </div>
</div>
</body>
</html>
```